Lanternfield Systems Bi Fold Brocher

I need a bi fold (front/back page 1 & front/back page 2) color brochure designed to pass out to clients at a convention. My website is lanternfieldsys.com. Please take images and text from the website to create the brochure. Use the products and product descriptions to display what we offer. Use the text and quotes to describe what we do. Make it professional, descriptive, and full of useful information.

Industry/Entity Type

Business Software

Font styles to use
Serif

Colors
00a990
33b8a4
86cfc6
fbf289
0255a3
3377b5
85acd3

Requirements
Must have
• Contact Info:
• Address:
• 287 Willowbend Avenue
• Building 700, Suite 3182
• Cumming, GA 30987
• Telephone: 1 (555) 482.7106
• Toll Free: 1 (800) 555.0147
• Email: contact@lanternfieldsys.com
Nice to have
• Good backrounds

```html
<!DOCTYPE html>
<html lang="en">
<head>
<meta charset="utf-8">
<title>Lanternfield Systems Brochure Spread</title>
<link href="https://fonts.googleapis.com/css2?family=Exo+2:ital,wght@1,500;1,600&family=Ubuntu:wght@400;500&display=swap" rel="stylesheet">
<style>
  :root {
    --stage: #b9b9b9;
    --teal: #17ad92;
    --teal-light: #2dbca4;
    --teal-dark: #1d7c76;
    --mint: #86cfc6;
    --cream: #f8f5d2;
    --mist: #e3f1f0;
    --lime: #eef28a;
    --ink: #2a3b3b;
    --white: #ffffff;
  }
  * { margin: 0; padding: 0; box-sizing: border-box; }
  html, body { width: 1200px; height: 900px; overflow: hidden; background: var(--stage); }
  .spread {
    position: absolute; left: 30px; top: 70px;
    width: 1140px; height: 760px;
    display: flex;
    box-shadow: 0 14px 30px rgba(0,0,0,.25);
  }
  .page { position: relative; width: 570px; height: 760px; overflow: hidden; }
  .page svg.bg { position: absolute; inset: 0; }

  /* Left page */
  .page--corporate { background: var(--teal); color: var(--white); font-family: "Ubuntu", sans-serif; }
  .section-title {
    position: absolute; font-family: "Exo 2", sans-serif; font-style: italic; line-height: 1;
    text-transform: uppercase;
  }
  .section-title .kicker { display: block; font-size: 17px; font-weight: 500; }
  .section-title .main { display: block; font-size: 27px; font-weight: 600; letter-spacing: .5px; }
  .page--corporate .section-title { left: 46px; top: 312px; }
  .intro {
    position: absolute; left: 46px; top: 370px; width: 505px;
    font-size: 11.6px; line-height: 17.4px; text-align: justify;
  }
  .values {
    position: absolute; left: 46px; top: 545px; width: 505px; list-style: none;
    font-size: 11.2px; line-height: 13.6px;
  }
  .values li { position: relative; padding-left: 30px; margin-bottom: 9px; text-align: justify; }
  .values li::before {
    content: ""; position: absolute; left: 0; top: 1px; width: 11px; height: 11px;
    border: 1.5px solid var(--lime); border-radius: 50%;
    background: radial-gradient(circle, var(--lime) 0 2.2px, transparent 2.6px);
  }

  /* Right page */
  .page--products { background: var(--white); color: var(--ink); font-family: "Ubuntu", sans-serif; }
  .page--products .section-title { left: 52px; top: 55px; color: var(--ink); }
  .product-label {
    position: absolute; right: 190px; font-size: 11px; font-weight: 500;
    letter-spacing: .3px; text-transform: uppercase;
  }
  .device { position: absolute; left: 402px; width: 130px; height: 108px; }
  .device .screen {
    position: absolute; right: 0; top: 0; width: 118px; height: 82px;
    border: 3px solid #111; background: linear-gradient(180deg, #f4f6f8 0 70%, #dfe6ea);
  }
  .device .tablet {
    position: absolute; left: 0; bottom: 0; width: 70px; height: 54px;
    border: 4px solid #111; border-radius: 3px;
    background: linear-gradient(180deg, #6f7a80, #3e474c);
  }
</style>
</head>
<body>
<div class="spread">

  <section class="page page--corporate">
    <svg class="bg" width="570" height="760" viewBox="0 0 570 760">
      <rect x="0" y="0" width="570" height="760" fill="var(--teal)"/>
      <rect x="0" y="515" width="570" height="245" fill="var(--teal-light)" opacity=".55"/>
      <path d="M485 300 Q470 530 500 760 L518 760 Q490 530 503 300 Z" fill="var(--white)" opacity=".08"/>
    </svg>
    <svg class="bg" width="570" height="760" viewBox="0 0 570 760" role="img" aria-label="Photo of a grey and yellow striped freight locomotive on desert tracks">
      <defs>
        <linearGradient id="photoTone" x1="0" y1="0" x2="0" y2="1">
          <stop offset="0" stop-color="#8ea3c4"/>
          <stop offset=".6" stop-color="#9aa0a4"/>
          <stop offset="1" stop-color="#b59d7e"/>
        </linearGradient>
      </defs>
      <path d="M105 60 Q300 -5 470 0 L490 0 Q300 15 130 80 Z" fill="var(--mint)" opacity=".7"/>
      <path d="M82 127 Q260 20 570 0 L570 235 Q560 300 525 328 Q260 300 82 127 Z" fill="url(#photoTone)"/>
      <path d="M525 328 Q560 300 570 235 L570 260 Q560 320 520 340 Q400 335 360 320 Q450 335 525 328 Z" fill="var(--mint)" opacity=".75"/>
    </svg>

    <h2 class="section-title"><span class="kicker">Corporate</span><span class="main">Overview</span></h2>
    <p class="intro">The Lanternfield Systems Training and Implementations Team has the primary focus of ensuring the success of our clients, and their use of Lanternfield Systems products to improve overall business processes. Our team is truly dedicated to focused, deliberate, and consultative services. With our customer-focused philosophy, we seek to always provide training and implementation services in such a way that encourages complete product utilization. We are always striving to learn and discover how to enhance the overall efficiency of our products. We are dedicated to making sure our customers have full operational visibility and realize true cost savings while using our product</p>
    <ul class="values">
      <li>Founded as a result of direct experience owning and managing a rail yard.</li>
      <li>Software cost must be scalable to the terminal that is using it.</li>
      <li>Open the lower end market and provide competitive pricing for the higher end market.</li>
      <li>Prepare our client to use the software and understand its functionality. The transition to our software must be easy and seamless. The client needs to understand completely and confidently how to use the software before purchasing it.</li>
      <li>Confirm and determine that the client understands the cost of the software upfront.</li>
      <li>Continue to grow our client base while never loosing the commitment to providing quick, honest answers, and cost effective solutions.</li>
      <li>Our current clients will attest to and our future clients will unquestionably receive the most user-friendly and robust software solutions available to manage their rail terminals.</li>
    </ul>
  </section>

  <section class="page page--products">
    <svg class="bg" width="570" height="760" viewBox="0 0 570 760">
      <ellipse cx="310" cy="300" rx="330" ry="300" fill="var(--cream)"/>
      <path d="M0 560 Q300 520 570 430 L570 760 H0 Z" fill="var(--mist)"/>
      <path d="M0 200 Q300 330 570 610 L570 650 Q300 380 0 250 Z" fill="var(--mist)" opacity=".8"/>
      <g fill="var(--teal-dark)">
        <path d="M0 137 H382 Q392 137 397 147 L417 202 H0 Z"/>
        <path d="M0 260 H382 Q392 260 397 270 L417 325 H0 Z"/>
        <path d="M0 383 H382 Q392 383 397 393 L417 448 H0 Z"/>
        <path d="M0 506 H382 Q392 506 397 516 L417 571 H0 Z"/>
        <path d="M0 629 H382 Q392 629 397 639 L417 694 H0 Z"/>
      </g>
    </svg>

    <h2 class="section-title"><span class="kicker">Products</span><span class="main">Overview</span></h2>

    <span class="product-label" style="top:118px">Railyard Inventory Software</span>
    <div class="device" style="top:98px" role="img" aria-label="Desktop and tablet showing the railyard inventory dashboard"><div class="screen"></div><div class="tablet"></div></div>

    <span class="product-label" style="top:241px">Railcar Inspection Software</span>
    <div class="device" style="top:221px" role="img" aria-label="Desktop and tablet showing the railcar inspection dashboard"><div class="screen"></div><div class="tablet"></div></div>

    <span class="product-label" style="top:364px">Transload Software</span>
    <div class="device" style="top:344px" role="img" aria-label="Desktop and tablet showing the transload dashboard"><div class="screen"></div><div class="tablet"></div></div>

    <span class="product-label" style="top:487px">Yardline Demurrage Software</span>
    <div class="device" style="top:467px" role="img" aria-label="Desktop and tablet showing the demurrage dashboard"><div class="screen"></div><div class="tablet"></div></div>

    <span class="product-label" style="top:610px">Rail EDI Messaging</span>
    <div class="device" style="top:590px" role="img" aria-label="Desktop and tablet showing the EDI messaging dashboard"><div class="screen"></div><div class="tablet"></div></div>
  </section>

</div>
</body>
</html>
```